Medical Billing - Professional Marketing Flier

We are needing help designing a clean and professional looking easy to read marketing flier for a medical billing practice. The text needs to be large enough to print. We are looking for a 5.5 x 8.5 design that we can edit the text as needed. I have included our logo and what we initially want it to say. Please keep in mind, we also want our logo and contact details on the flier. Let me know if you have any questions.

```html
<!DOCTYPE html>
<html lang="en">
<head>
<meta charset="utf-8">
<title>Vega Health Billing – Flier</title>
<link rel="stylesheet" href="https://fonts.googleapis.com/css2?family=Poppins:wght@300;400&family=Tinos:wght@700&display=swap">
<style>
  :root {
    --backdrop: #b1b7be;
    --pink: #be62a6;
    --ink: #000000;
    --paper: #ffffff;
    --text: #1e1e1e;
    --photo-light: #f1f2f3;
    --photo-mid: #c9d1d4;
    --photo-teal: #2f6f72;
  }
  * { margin: 0; padding: 0; box-sizing: border-box; }
  html, body {
    width: 982px; height: 1200px; overflow: hidden;
    background: var(--backdrop);
  }
  .flier {
    position: absolute; left: 175.4px; top: 111.4px;
    width: 1116px; height: 1740px;
    transform: scale(0.5657); transform-origin: 0 0;
    background: var(--paper);
    font-family: "Poppins", sans-serif;
    color: var(--text);
    overflow: hidden;
  }
  .backdrop-shapes { position: absolute; left: 0; top: 0; width: 1116px; height: 1740px; }
  .photo-panel {
    position: absolute; left: 0; top: 300px; width: 364px; height: 1426px;
    background: linear-gradient(180deg, var(--photo-light) 0%, var(--photo-mid) 30%, var(--photo-teal) 55%, var(--photo-mid) 75%, var(--photo-light) 100%);
  }
  .brand-name {
    position: absolute; left: 60px; top: 120px; width: 420px; z-index: 2;
    font-family: "Tinos", serif; font-weight: 700; font-size: 56px; line-height: 1.05;
    color: var(--pink); text-align: center;
  }
  .headline {
    position: absolute; left: 677px; top: 38px;
    font-family: "Tinos", serif; font-weight: 700; font-size: 43px; line-height: 45px;
    color: var(--paper); letter-spacing: 0.5px;
  }
  .service { position: absolute; left: 400px; width: 680px; }
  .service-thumb {
    position: absolute; left: 0; top: 3px; width: 136px; height: 172px;
    border-radius: 28px 0 0 0;
  }
  .thumb-invoice { background: linear-gradient(160deg, #e9edf2 0%, #ffffff 45%, #cfd6df 100%); }
  .thumb-aging { background: linear-gradient(170deg, #5f7a45 0%, #3d4f34 55%, #2b3340 100%); }
  .thumb-credential { background: linear-gradient(160deg, #4d5d7e 0%, #b9c4cf 50%, #e6eef0 100%); }
  .service-body { margin-left: 158px; }
  .service-title {
    font-family: "Tinos", serif; font-weight: 700; font-size: 39px; line-height: 42px;
    color: var(--pink); letter-spacing: 0.5px;
  }
  .service-text {
    font-size: 18.6px; line-height: 28.6px; font-weight: 400;
    text-align: justify; margin-top: 2px; letter-spacing: -0.45px;
  }
  .contact-title {
    position: absolute; left: 364px; width: 752px; top: 1246px;
    font-family: "Tinos", serif; font-weight: 700; font-size: 39px;
    color: var(--pink); text-align: center; letter-spacing: 0.5px;
  }
  .contact-box {
    position: absolute; left: 400px; top: 1307px; width: 680px; min-height: 179px;
    background: var(--pink); color: var(--paper);
    padding: 18px 26px; font-size: 18.6px; line-height: 28.6px;
    text-align: justify; letter-spacing: -0.45px;
  }
  .contact-bar {
    position: absolute; left: 364px; top: 1515px; width: 752px; height: 135px;
    background: var(--ink); color: var(--paper);
  }
  .contact-divider {
    position: absolute; left: 292px; top: 18px; width: 2px; height: 99px; background: var(--paper);
  }
  .contact-item { position: absolute; display: flex; align-items: center; gap: 16px; white-space: nowrap; }
  .contact-item svg { flex: none; }
  .contact-phone { left: 40px; top: 48px; font-size: 27px; }
  .contact-email { left: 312px; top: 28px; font-size: 20px; }
  .contact-address { left: 312px; top: 73px; font-size: 20px; }
  .web-band {
    position: absolute; left: 364px; top: 1650px; width: 752px; height: 76px;
    background: var(--pink); color: var(--paper);
    font-size: 33px; line-height: 76px; text-align: center;
  }
</style>
</head>
<body>
<main class="flier">
  <svg class="backdrop-shapes" viewBox="0 0 1116 1740" aria-hidden="true">
    <rect x="364" y="0" width="752" height="420" fill="var(--pink)"/>
    <path d="M364 320 Q740 200 1116 320 V1726 H364 Z" fill="var(--paper)"/>
  </svg>
  <div class="photo-panel" role="img" aria-label="Photo of a stethoscope resting on a medical billing form"></div>
  <svg class="backdrop-shapes" viewBox="0 0 1116 1740" aria-hidden="true" style="z-index:1">
    <path d="M0 0 H650 C620 200 420 350 0 351 Z" fill="var(--ink)"/>
  </svg>

  <div class="brand-name">Vega Health Billing</div>

  <h1 class="headline">MEDICAL BILLING<br>TAILORED<br>TO YOUR<br>PRACTICES NEEDS</h1>

  <section class="service" style="top:315px">
    <div class="service-thumb thumb-invoice" role="img" aria-label="Sample patient invoice document"></div>
    <div class="service-body">
      <h2 class="service-title">MEDICAL BILLING</h2>
      <p class="service-text">Would you prefer to spend time focusing on your clients and running your practice rather than trying to stay up to speed with the constantly changing medical billing rules and regulations? Let us help you by managing your medical billing and dealing with the insurance companies on your behalf! We work with you to tailor the entire medical billing process to suit your practices needs while making it as smooth and painless as possible.</p>
    </div>
  </section>

  <section class="service" style="top:650px">
    <div class="service-thumb thumb-aging" role="img" aria-label="Older couple walking in a garden"></div>
    <div class="service-body">
      <h2 class="service-title">AGING</h2>
      <p class="service-text">Are you leaving money on the table? Are you able to do the follow-through needed to keep your aging in check and more money flowing into your practice? Are you uncertain about how to get insurance to pay on claims that should be covered but for some reason they decided not to? We can clean up your aging, reduce the amount of time it takes for claims to pay out, and we can keep your aging to a minimum.</p>
    </div>
  </section>

  <section class="service" style="top:954px">
    <div class="service-thumb thumb-credential" role="img" aria-label="Hand signing a contract with a pen"></div>
    <div class="service-body">
      <h2 class="service-title">CREDENTIALING</h2>
      <p class="service-text">Are you wanting to get contracted with insurance companies but aren't sure how to go about it? Are you wanting to expand your client base by having the option to bill insurance? Let us take the confusion out of what can seem like a daunting task! We can get you and your practitioners contracted with the insurance companies of your choice and help you navigate through the process every step of the way!</p>
    </div>
  </section>

  <h2 class="contact-title">CONTACT US</h2>
  <p class="contact-box">If any of these processes are something you would like our help with or to consult with us on, please email us or give us a call! We specialize in billing and contracting for Nutritionists and Dietitians. We would love to help you expand your business and take the pain and frustration out of billing so you can focus on your clients.</p>

  <footer class="contact-bar">
    <div class="contact-item contact-phone">
      <svg width="32" height="32" viewBox="0 0 24 24" aria-hidden="true"><path d="M6.6 10.8a15 15 0 0 0 6.6 6.6l2.2-2.2a1 1 0 0 1 1-.25 11.4 11.4 0 0 0 3.6.57 1 1 0 0 1 1 1V20a1 1 0 0 1-1 1A17 17 0 0 1 3 4a1 1 0 0 1 1-1h3.5a1 1 0 0 1 1 1c0 1.25.2 2.45.57 3.57a1 1 0 0 1-.25 1z" fill="#fff"/><path d="M14 3a7 7 0 0 1 7 7M14 6.5a3.5 3.5 0 0 1 3.5 3.5" stroke="#fff" stroke-width="1.6" fill="none"/></svg>
      <span>555-014-2278</span>
    </div>
    <div class="contact-divider"></div>
    <div class="contact-item contact-email">
      <svg width="30" height="22" viewBox="0 0 30 22" aria-hidden="true"><rect x="1" y="1" width="28" height="20" fill="#fff"/><path d="M1 1 L15 13 L29 1 M1 21 L11 10 M29 21 L19 10" stroke="#000" stroke-width="2" fill="none"/></svg>
      <span>hello@vegahealthbilling.com</span>
    </div>
    <div class="contact-item contact-address">
      <svg width="30" height="34" viewBox="0 0 24 28" aria-hidden="true"><path d="M12 1a9 9 0 0 0-9 9c0 7 9 17 9 17s9-10 9-17a9 9 0 0 0-9-9z" fill="#fff"/><circle cx="12" cy="10" r="3.5" fill="#000"/></svg>
      <span>PO Box 410 Cedar Falls, WA 98000</span>
    </div>
  </footer>
  <div class="web-band">www.vegahealthbilling.com</div>
</main>
</body>
</html>
```